Book Cover for Adult Coloring Book

I'd like a unique book cover design for a coloring book we are making for adults. The book cover is for an 8.5"x11" book. I need both the front and back cover created. We will want to include some text about the book on the back cover so there should be room for that. It will be less than 100 words.

1) The title is:

Grown-Up Doodle Pages: Cheeky Phrases To Leave Every Jaw Hanging Open

2) A swear word may appear on the cover, however it should similar to some of the examples included.

3) I'd prefer the background be in black or white so that the picture and color "pop" off the page more.

I've included 4 example covers that I really like. Something similar to these is preferred.

Reason: I've had a designer ask if we could extend the deadline. I'd like to get as many options as possible since this is a guaranteed project. Please extend it to Friday, February 19th, 2016. I may choose someone before then, but I'd like to see as many as possible before I do. Thank you, Marcus

Target Market(s)

Adults 25-65

Industry/Entity Type

Publishing Company

Font styles to use
Sans Serif
Decorative
Script

Requirements
Must have
• Unique design and be colorful. It's okay to have a swear word but it should be subtle and similar in design to some of the examples I provided.
Nice to have
• Black or white background that will allow the image/text to "pop" on the page.
Should not have
• No slurs, racial or homophobic words.

```html
<!DOCTYPE html>
<html lang="en">
<head>
<meta charset="utf-8">
<title>Grown-Up Doodle Pages — Cover Spread</title>
<link href="https://fonts.googleapis.com/css2?family=Anton&family=Bebas+Neue&family=Kaushan+Script&family=Open+Sans:wght@600&family=Oswald:wght@400&display=swap" rel="stylesheet">
<style>
  :root {
    --paper: #ffffff;
    --plum: #962a86;
    --ink: #000000;
    --pink: #e2458f;
    --magenta: #c8329a;
    --violet: #8a4fb0;
    --lime: #a9c93a;
    --amber: #e8a23a;
    --teal: #3aa6a0;
    --red: #e23a4a;
  }
  * { margin: 0; padding: 0; box-sizing: border-box; }
  html, body { width: 1200px; height: 927px; overflow: hidden; background: var(--paper); }
  .cover-spread { position: relative; width: 1200px; height: 927px; background: var(--paper); }

  .back-blurb {
    position: absolute; left: 48px; top: 56px; width: 520px;
    font-family: "Kaushan Script", cursive; font-size: 45px; line-height: 56px; white-space: nowrap;
    background: linear-gradient(90deg, var(--violet), var(--teal), var(--lime), var(--amber), var(--pink), var(--violet));
    -webkit-background-clip: text; background-clip: text; color: transparent;
  }
  .back-art { position: absolute; left: 62px; top: 192px; width: 462px; height: 448px; }

  .spine-title {
    position: absolute; left: 600px; top: 464px;
    transform: translate(-50%, -50%) rotate(-90deg);
    font-family: "Oswald", sans-serif; font-size: 50px; letter-spacing: 0.5px;
    color: var(--plum); white-space: nowrap; line-height: 1;
  }

  .series-line {
    position: absolute; left: 676px; top: 32px; width: 480px; text-align: center;
    font-family: "Open Sans", sans-serif; font-weight: 600; font-size: 33px; letter-spacing: 1px;
    background: linear-gradient(90deg, #c98a3a, #b07a6a, #7fa35a, #d0a050, #b06a8a);
    -webkit-background-clip: text; background-clip: text; color: transparent; white-space: nowrap;
  }
  .main-title {
    position: absolute; left: 672px; top: 78px; width: 484px; text-align: center;
    font-family: "Bebas Neue", sans-serif; font-size: 100px; line-height: 100px;
    color: var(--plum); white-space: nowrap; letter-spacing: -1px;
  }
  .front-art { position: absolute; left: 656px; top: 192px; width: 536px; height: 616px; }
  .tagline-band {
    position: absolute; left: 656px; top: 386px; width: 504px; height: 62px;
    background: var(--paper); display: flex; align-items: center; justify-content: center;
  }
  .tagline {
    font-family: "Kaushan Script", cursive; font-size: 30px; color: var(--ink); white-space: nowrap;
  }
  .author-name {
    position: absolute; left: 676px; top: 836px; width: 476px; text-align: center;
    font-family: "Anton", sans-serif; font-size: 58px; line-height: 72px; color: var(--ink); letter-spacing: 1px;
  }
</style>
</head>
<body>
<main class="cover-spread">
  <section class="back-cover">
    <p class="back-blurb">Lorem ipsum dolor sit amet,<br>consectetur adipisicing elit,</p>
    <svg class="back-art" viewBox="0 0 462 448" role="img" aria-label="Colourful doodle pattern of paisley leaves, swirls and hearts on white">
      <defs>
        <linearGradient id="backArtFill" x1="0" y1="0" x2="1" y2="1">
          <stop offset="0" stop-color="#c86ab0"/>
          <stop offset="0.18" stop-color="#f0c6dc"/>
          <stop offset="0.32" stop-color="#e2458f"/>
          <stop offset="0.46" stop-color="#a9c93a"/>
          <stop offset="0.58" stop-color="#f3d9ea"/>
          <stop offset="0.7" stop-color="#c8329a"/>
          <stop offset="0.84" stop-color="#8a4fb0"/>
          <stop offset="1" stop-color="#e8a23a"/>
        </linearGradient>
      </defs>
      <path fill="url(#backArtFill)" d="M90 45 C120 25 170 35 200 30 C230 20 270 10 300 20 C320 0 345 5 345 30 C350 45 335 55 325 60 C350 65 375 85 385 110 C410 115 440 135 445 165 C455 200 440 240 448 280 C450 310 430 320 435 345 C410 370 400 395 370 405 C340 425 300 430 265 440 C230 450 200 440 175 430 C140 428 120 410 100 385 C70 370 55 345 45 320 C20 300 10 270 15 240 C5 215 20 190 40 175 C25 150 35 130 55 125 C50 100 60 70 90 45 Z"/>
    </svg>
  </section>

  <div class="spine-title">GROWN-UP DOODLE PAGES</div>

  <section class="front-cover">
    <p class="series-line">GROWN-UP DOODLE PAGES</p>
    <h1 class="main-title">CHEEKY PHRASES</h1>
    <svg class="front-art" viewBox="0 0 536 616" role="img" aria-label="Colourful doodle pattern of paisley leaves, swirls and hearts around the tagline">
      <defs>
        <linearGradient id="frontArtFill" x1="0" y1="0" x2="1" y2="1">
          <stop offset="0" stop-color="#e2458f"/>
          <stop offset="0.14" stop-color="#f4d3e6"/>
          <stop offset="0.26" stop-color="#a9c93a"/>
          <stop offset="0.38" stop-color="#e23a4a"/>
          <stop offset="0.5" stop-color="#c8329a"/>
          <stop offset="0.62" stop-color="#f3e0ec"/>
          <stop offset="0.74" stop-color="#8a4fb0"/>
          <stop offset="0.86" stop-color="#a9c93a"/>
          <stop offset="1" stop-color="#c8329a"/>
        </linearGradient>
      </defs>
      <path fill="url(#frontArtFill)" d="M115 5 C150 -5 185 15 190 45 C205 40 215 60 200 75 C215 95 230 70 240 50 C255 20 300 15 320 40 C345 20 385 20 400 45 C430 40 460 60 470 95 C500 110 520 140 515 180 C530 200 535 230 520 250 L520 300 C505 330 500 360 520 380 C536 410 530 440 510 455 C520 480 510 520 480 530 C470 560 440 580 400 575 C370 600 330 610 300 595 C260 612 220 605 200 585 C170 600 130 590 120 560 C100 540 100 510 115 490 C95 475 90 450 110 430 C85 410 70 385 80 360 C50 355 20 340 15 310 C0 285 10 255 40 245 C45 230 65 220 85 215 C90 190 110 175 130 170 C105 140 95 100 105 70 C95 45 95 20 115 5 Z"/>
    </svg>
    <div class="tagline-band">
      <p class="tagline">To Leave Every Jaw Hanging Open</p>
    </div>
    <p class="author-name">AUTHOR NAME</p>
  </section>
</main>
</body>
</html>
```